New flavour! New packaging for Velocity Energy Drink!

We need a new packaging designed to show off our new grape flavored energy drink! It will require box design with matching sachets!

Established in 2018 we are a fully Australian owned and operated business that started out with 2 gamers that got sick and tired of sugary energy drinks OR expensive powder from the USA.

We are an energy drink in the esports and gaming space. Our new product is an energy drink in powder in boxes of 30 sachets (please see attached for product example)

Please see example 1 and 2 for our competitors product. We would ideally like to go a bit more minimalist than them but still have a great color pop on black backing.

Target Market(s)

Gamer's and esports athletes between the ages or 18-30

Font styles to use
Sans Serif
Other font styles liked:
• Helvetica

Colors
886aae
ffffff

Requirements
Must have
• Black base/background.
• Vibrant purple N in the Velocity Logo.
• Same or slightly different shades of purple for some text and highlights.
• Black, white and some shades of a vibrant purple (for the grape flavor)
• ingredients list (may need to be reformatted to suit)
• Please see attached for legislative requirements on the box and sachets.
Nice to have
• minimalist design but enough to be eye catching and somewhat playful
• Twitter: @VLCT_FUEL
• Instagram: @VLCT_FUEL
• Facebook: @VLCTFUEL
Should not have
• OTHER COLORS.
• Overly complex designs.

```html
<!DOCTYPE html>
<html lang="en">
<head>
<meta charset="utf-8">
<title>Velocity Energy Drink – Grape Box &amp; Sachet</title>
<link href="https://fonts.googleapis.com/css2?family=Archivo+Black&family=Montserrat:wght@400;600;800;900&family=Allura&display=swap" rel="stylesheet">
<style>
  :root{
    --grape:#886aae;
    --grape-deep:#6f4f9a;
    --grape-light:#a48bc6;
    --black:#111111;
    --white:#ffffff;
    --panel:#f2f2f4;
    --rule:#c9c9cf;
    --backdrop:#e8e172;
  }
  *{margin:0;padding:0;box-sizing:border-box}
  html,body{width:1200px;height:1056px;overflow:hidden}
  body{background:var(--backdrop);font-family:"Montserrat",Helvetica,Arial,sans-serif;position:relative}

  .vertical-up{position:absolute;writing-mode:vertical-rl;transform:rotate(180deg);white-space:nowrap}
  .vertical-down{position:absolute;writing-mode:vertical-rl;white-space:nowrap}

  /* ---------- box side panel ---------- */
  .box-side{position:absolute;left:130px;top:220px;width:270px;height:640px;background:linear-gradient(180deg,var(--white),var(--panel));border:1px solid var(--rule);padding:28px 16px;font-size:8.5px;color:#333;line-height:1.55}
  .nutrition-title{background:var(--grape);color:var(--white);font-weight:800;font-size:9px;padding:3px 6px;border-radius:0 8px 8px 0;width:78%;margin-bottom:8px}
  .nutrition-table{width:100%;border-collapse:collapse;font-size:8px;table-layout:fixed}
  .nutrition-table col.label{width:46%}
  .nutrition-table col.value{width:27%}
  .nutrition-table td{padding:1.5px 2px;white-space:nowrap}
  .nutrition-table td+td{text-align:right}
  .nutrition-table .indent td:first-child{padding-left:12px}
  .nutrition-table .head td{font-weight:700;font-size:6.5px;border-bottom:1px solid var(--rule)}
  .nutrition-table .serving td:last-child{text-align:right}
  .ingredients{margin-top:12px;font-size:8px;line-height:1.55}

  /* ---------- box front panel ---------- */
  .box-front{position:absolute;left:400px;top:220px;width:340px;height:640px;background:var(--white);overflow:hidden;border:1px solid var(--rule)}
  .box-front .black-field{position:absolute;inset:0}
  .brand-name{font-family:"Archivo Black",sans-serif;font-size:60px;letter-spacing:-1px;color:var(--black);line-height:1}
  .brand-sub{font-weight:800;font-size:10px;letter-spacing:3px;color:var(--black);line-height:1}
  .flavour{font-weight:900;font-size:24px;color:var(--grape);line-height:1}
  .script{font-family:"Allura",cursive;font-size:28px;color:var(--black);line-height:1}

  .claims{position:absolute;left:170px;top:36px;display:flex;flex-direction:column;gap:14px}
  .claim{width:70px;height:70px;border-radius:50%;background:var(--white);border:3px solid #b9b9c0;box-shadow:0 0 0 2px var(--black);display:flex;flex-direction:column;align-items:center;justify-content:center;text-align:center;font-weight:900;font-size:9.5px;line-height:1.05;color:var(--black)}
  .claim svg{margin-bottom:3px}
  .claim .zero{font-size:20px;color:var(--grape)}

  .headline{font-family:"Archivo Black",sans-serif;font-size:66px;color:var(--grape);-webkit-text-stroke:2px #d8d8dd;letter-spacing:1px;line-height:1}

  .count{position:absolute;left:18px;top:470px;text-align:center;width:96px}
  .count .num{font-family:"Archivo Black",sans-serif;font-size:32px;color:var(--black);line-height:1}
  .count .unit{font-weight:900;font-size:14px;color:var(--grape)}
  .count .tag{font-weight:800;font-size:8px;color:var(--black)}

  .grape-art{position:absolute;border-radius:44% 44% 50% 50%/40% 40% 60% 60%;background:radial-gradient(circle at 40% 35%,var(--grape-light),var(--grape) 55%,var(--grape-deep))}

  /* ---------- sachet ---------- */
  .sachet{position:absolute;left:900px;top:150px;width:180px;height:740px;background:var(--white);overflow:hidden;border:1px solid var(--rule)}
  .sachet .black-field{position:absolute;inset:0;width:100%;height:100%}
  .sachet .crimp{position:absolute;left:0;right:0;height:22px;background:repeating-linear-gradient(90deg,rgba(0,0,0,.08) 0 2px,transparent 2px 5px)}
  .sachet .crimp.top{top:0}
  .sachet .crimp.bottom{bottom:0}
  .sachet .brand-name{font-size:34px}
  .sachet .brand-sub{font-size:6.5px;letter-spacing:2px}
  .sachet .headline{font-size:62px}
  .sachet .flavour{font-size:18px;color:var(--white)}
  .sachet .script{font-size:20px}
  .sachet-tag{position:absolute;left:48px;bottom:34px;font-weight:900;font-size:11px;color:var(--grape);line-height:1.15}
</style>
</head>
<body>

<!-- Box side: nutrition & ingredients -->
<section class="box-side">
  <div class="nutrition-title">NUTRITION INFORMATION</div>
  <table class="nutrition-table">
    <colgroup><col class="label"><col class="value"><col class="value"></colgroup>
    <tr><td>SERVINGS PER PACKAGE:</td><td>30</td><td></td></tr>
    <tr class="serving"><td>SERVING SIZE:</td><td colspan="2">5g powder &amp; 500 ml water</td></tr>
    <tr class="head"><td></td><td>AV. QTY PER SERVING</td><td>AV. QTY PER 100 ml</td></tr>
    <tr><td>ENERGY</td><td>5 kJ</td><td>1 kJ</td></tr>
    <tr><td>PROTEIN</td><td>0.0 g</td><td>0.0 g</td></tr>
    <tr><td>FAT, TOTAL</td><td>0.0 g</td><td>0.0 g</td></tr>
    <tr class="indent"><td>Saturated Fat</td><td>0.0 g</td><td>0.0 g</td></tr>
    <tr><td>CARBOHYDRATE</td><td>0.0 g</td><td>0.0 g</td></tr>
    <tr class="indent"><td>Sugars</td><td>0.0 g</td><td>0.1 g</td></tr>
    <tr><td>SODIUM</td><td>250 mg</td><td>62 mg</td></tr>
    <tr class="head"><td>Composition Information</td><td></td><td></td></tr>
    <tr><td>Caffeine</td><td>100 mg</td><td>25 mg</td></tr>
    <tr><td>Thiamin (B1)</td><td>10 mg</td><td>2.5 mg</td></tr>
    <tr><td>Riboflavin (B2)</td><td>5 mg</td><td>1.2 mg</td></tr>
    <tr><td>Niacin (B3)</td><td>20 mg</td><td>5 mg</td></tr>
    <tr><td>B6 (Pyridoxine)</td><td>5 mg</td><td>1.2 mg</td></tr>
    <tr><td>Taurine</td><td>500 mg</td><td>125 mg</td></tr>
    <tr><td>Inositol</td><td>50 mg</td><td>12.5 mg</td></tr>
  </table>
  <p class="ingredients">Ingredient listing: Acidity regulator (citric acid), sodium citrate, natural grape flavour, taurine, inositol, caffeine, ginseng extract, vitamins (B3, B6, B2, B1), sweetener (sucralose), colour (anthocyanin), anti-caking agent (silicon dioxide), magnesium stearate.</p>
</section>

<!-- Box front -->
<section class="box-front">
  <svg class="black-field" viewBox="0 0 340 640" preserveAspectRatio="none" aria-hidden="true">
    <path d="M175 0 C120 110 235 210 160 330 C100 430 140 540 120 640 L340 640 L340 0 Z" fill="var(--black)"/>
  </svg>

  <div class="vertical-up brand-name" style="left:24px;top:40px">VELOCITY</div>
  <div class="vertical-up brand-sub" style="left:88px;top:40px">ENERGY DRINK</div>
  <div class="vertical-up flavour" style="left:102px;top:30px">grape flavored drink</div>
  <div class="vertical-up script" style="left:134px;top:56px">With Ginseng &amp; Caffeine</div>

  <div class="claims">
    <div class="claim">
      <svg width="16" height="20" viewBox="0 0 16 20"><path d="M10 0 L1 11 H7 L5 20 L15 8 H9 Z" fill="var(--grape)"/></svg>
      ENERGY<br>BOOST
    </div>
    <div class="claim"><span class="zero">0</span>ZAERO<br>FATS</div>
    <div class="claim">
      <svg width="22" height="18" viewBox="0 0 22 18"><circle cx="11" cy="9" r="4" fill="var(--grape)"/><circle cx="3" cy="3" r="2.5" fill="var(--grape)"/><circle cx="19" cy="3" r="2.5" fill="var(--grape)"/><circle cx="11" cy="16" r="2" fill="var(--grape)"/><path d="M4 4 L9 8 M18 4 L13 8 M11 13 V15" stroke="var(--grape)" stroke-width="1.5"/></svg>
      AMINO<br>ACID
    </div>
    <div class="claim">
      <svg width="18" height="18" viewBox="0 0 18 18"><path d="M2 16 C2 6 8 2 16 2 C16 10 12 16 2 16 Z" fill="var(--grape)"/></svg>
      VEGAN
    </div>
  </div>

  <div class="vertical-down headline" style="left:264px;top:18px">ENERGY DRINK</div>

  <div class="count">
    <div class="num">30</div>
    <div class="unit">SACHET</div>
    <div class="tag">FOR GAMERS,<br>BY GAMERS</div>
  </div>

  <div class="grape-art" role="img" aria-label="Illustrated bunch of purple grapes with a green leaf" style="left:150px;top:420px;width:120px;height:190px"></div>
</section>

<!-- Sachet -->
<section class="sachet">
  <svg class="black-field" viewBox="0 0 180 740" preserveAspectRatio="none" aria-hidden="true">
    <path d="M95 0 C60 90 120 170 80 280 C50 380 90 440 70 740 L180 740 L180 0 Z" fill="var(--black)"/>
  </svg>
  <div class="crimp top"></div>
  <div class="crimp bottom"></div>

  <div class="vertical-up brand-name" style="left:12px;top:210px">VELOCITY</div>
  <div class="vertical-up brand-sub" style="left:50px;top:230px">ENERGY DRINK</div>
  <div class="vertical-down headline" style="left:72px;top:120px">ENERGY</div>
  <div class="vertical-down flavour" style="left:146px;top:120px">grape flavored drink</div>
  <div class="vertical-up script" style="left:14px;top:470px">With Ginseng &amp; Caffeine</div>

  <div class="grape-art" role="img" aria-label="Illustrated bunch of purple grapes with a green leaf" style="left:58px;top:520px;width:92px;height:120px"></div>
  <div class="sachet-tag">FOR GAMERS,<br>BY GAMERS</div>
</section>

</body>
</html>
```